Home Page Design for Motor Manufacturer

Hello,
please design the homepage for a manufacturer of industry motors. I am looking for a professional, clean and minimalistic design. Since this a rather conservative industry it should get a professional look but since it is a redesign there should be some modern that gives is the modern touch of innovation.
A competitor's homepage I like is:
https://www.valtrosk.com/en/
What I like about this website:
* clean, minimal, well structured design
* mega menu
For this project please find attached the wireframes (most buttons are in German but by context and Google translate you will easily figure it out; only unclear - "Messe" means "trade exhibition"). The paddings and margins are NOT exact. Also any color of backgrounds etc. chosen is not meant to represent a real color but rather to illustrate the object and maybe show there should be some background emphasis (color or image).
Wireframes:
https: //www.filmavek. com / t / pxuTQmD7ZJHaLrwY
In both wireframes the only thing that is different is the Service section. I expect from the winner both designs for this service section: one with normal cart design and one with tabs as filters to search products (find image for product categories attached)
In the header use on the left the following text:
h1: "Your competent partner for industrial engines,
-transmission and drawing parts
with more than 5000 satisfied customers "
primary button: Our products
sec. button: Download catalog
and on the right side we feature one or more product images (like putting them in a nice display together).
I also think of a solid background color or subtle gradient for the hero section.
The winner should also design an open mega menu version.
Menu items in this order:
• Home page
• Gearboxes & Motors
• Engine components
• Drawing parts
• Machines & accessories
• About us
• Contact
Also create a language switch with globe symbol and DE for Germany and EN for English above the nav plus the telephone number with icon (user dummy number +49 (0) 987654321)
Output should be in Figma, Sketch or PSD.
Fonts + color to use:
header: Proza Libre, bold, # 0171A1
body: Open Sans, regular, black
Primary accent color: # 0171A1
Text black or dark gray
background: light gray, white or shade of blue
More image resources:
https://www.filmavek.com/t/QrnLVdHZPKEX1bmu
If there are any questions please do not hesitate to ask.
Target Market(s)
B2B - anyone with industrial machinery needing small motors (not car engines)
Industry/Entity Type
Manufacturing
Number of Pages Required
1 page
Requirements
Must have
- see above
Nice to have
- see above
Should not have
- see above

```html
<!DOCTYPE html>
<html lang="en">
<head>
<meta charset="utf-8">
<title>KVR – Industrial Motors</title>
<link href="https://fonts.googleapis.com/css2?family=Open+Sans:wght@400;600;700&family=Proza+Libre:wght@500;600;700&display=swap" rel="stylesheet">
<style>
:root{
  --blue:#0171A1;
  --blue-dark:#0b5d88;
  --navy:#0d4468;
  --ink:#222;
  --gray:#555;
  --light:#f0f0f0;
  --white:#fff;
}
*{margin:0;padding:0;box-sizing:border-box}
html,body{width:1200px;height:3850px;overflow:hidden}
body{position:relative;font-family:"Open Sans",sans-serif;color:var(--ink);background:var(--white)}
.abs{position:absolute}
h1,h2,h3{font-family:"Proza Libre",sans-serif}

/* top bar */
.topbar{left:0;top:0;width:1200px;height:81px;background:var(--white)}
.lang{left:120px;top:27px;width:72px;height:28px;border:1px solid #ddd;border-radius:3px}
.lang .flag{position:absolute;left:6px;top:6px;width:30px;height:16px;background:linear-gradient(#c8102e,#1e3a8a)}
.lang .caret{position:absolute;left:50px;top:11px;border:6px solid transparent;border-top-color:#888}
.brand{left:0;width:1200px;top:8px;text-align:center;font-family:"Proza Libre",sans-serif;font-weight:700;font-size:56px;color:var(--navy);letter-spacing:2px;line-height:64px}
.call{left:896px;top:18px;display:flex;gap:14px;align-items:center;font-size:14px}
.call small{display:block;font-size:13px;color:#333}
.call b{font-size:16px;font-weight:600}

/* hero */
.hero{left:0;top:81px;width:1200px;height:670px}
.nav{left:118px;top:105px;display:flex;gap:32px;color:var(--white);font-size:15px}
.nav span.dd::after{content:"";display:inline-block;margin-left:6px;border:4px solid transparent;border-top-color:rgba(255,255,255,.7);vertical-align:-1px}
.hero-title{left:121px;top:292px;color:var(--white);font-size:38px;line-height:51px;font-weight:700}
.hero-sub{left:121px;top:420px;color:var(--white);font-size:21px;line-height:36px}
.btn-hero{left:121px;top:521px;width:152px;height:40px;border-radius:20px;background:#0a8fc2;color:#fff;font-size:17px;text-align:center;line-height:40px}

/* why */
.section-title{width:1200px;left:0;text-align:center;font-weight:500;color:var(--ink)}
.why-text{left:250px;width:700px;top:883px;text-align:center;font-size:15px;line-height:27px;color:#333}
.feature{display:flex;align-items:center;gap:18px;top:1009px;font-size:21px;line-height:27px;color:#333}

/* products */
.products-bg{left:0;top:1204px;width:1200px;height:631px;background:var(--light)}
.card{background:var(--white);text-align:center}
.card .img{position:absolute;left:50%;transform:translateX(-50%);width:170px;height:130px;top:28px;border-radius:50%;background:radial-gradient(circle,#6b7a88,#cfd5da 60%,transparent 72%)}
.card h3{position:absolute;width:100%;font-size:19px;font-weight:600;color:var(--ink)}
.pill{position:absolute;left:50%;transform:translateX(-50%);width:110px;height:27px;border-radius:14px;background:#666;color:#fff;font-size:14px;line-height:27px;text-align:center}
.card.active{background:var(--blue)}
.card.active h3{color:#fff}
.card.active .pill{background:var(--navy)}
.dot{width:13px;height:13px;border-radius:50%;border:1.5px solid #999;top:1718px}

/* trade */
.tile{background:#f3f3f3}
.photo{display:block}
.tile h3{font-family:"Open Sans",sans-serif;font-size:17px;font-weight:600;color:var(--ink);position:absolute;left:29px}
.tile p{position:absolute;left:29px;width:230px;font-size:13px;line-height:24px;color:#444}
.tbtn{position:absolute;height:31px;line-height:31px;color:#fff;font-size:15px;text-align:center}
.tbtn.ticket{background:var(--blue);width:112px}
.tbtn.more{background:var(--navy);width:90px}
.view-more{left:523px;top:2473px;width:154px;height:47px;background:var(--navy);color:#fff;font-size:19px;line-height:47px;text-align:center}

/* ebook */
.ebook-head{left:462px;top:2660px;color:#fff;font-size:35px;font-weight:500;letter-spacing:.5px}
.ebook-sub{left:462px;top:2710px;color:#fff;font-size:19px}
.btn-dl{left:462px;top:2753px;width:168px;height:39px;border-radius:20px;background:#111;color:#fff;font-size:15px;font-weight:600;text-align:center;line-height:39px}

/* about */
.about-bg{left:0;top:2940px;width:1200px;height:546px}
.about-box{left:336px;top:3043px;width:529px;height:313px;background:rgba(255,255,255,.95);border:2px solid var(--blue);padding:36px 55px}
.about-box h2{font-size:37px;font-weight:500;margin-bottom:20px}
.about-box p{font-size:15px;line-height:26px;color:#333;margin-bottom:17px}

/* footer */
.footer{left:0;top:3486px;width:1200px;height:364px;background:var(--blue)}
.footer-bar{left:0;top:3780px;width:1200px;height:70px;background:var(--blue-dark)}
.f-brand{left:120px;top:3568px;width:212px;font-family:"Proza Libre",sans-serif;font-weight:700;font-size:82px;color:#fff;letter-spacing:2px;line-height:90px;text-align:center}
.social{top:3704px;width:18px;height:18px;border-radius:50%;border:2px solid #fff}
.f-col{color:#fff;font-size:14px;line-height:24px}
.f-col h4{font-size:16px;font-weight:600;margin-bottom:12px}
.f-row{display:flex;gap:14px;margin-bottom:10px}
.btn-contact{left:862px;top:3684px;width:176px;height:42px;border-radius:21px;background:var(--navy);color:#fff;font-size:16px;line-height:42px}
.copy{left:142px;top:3806px;color:#fff;font-size:15px}
.legal{left:840px;top:3807px;color:#fff;font-size:14px}
</style>
</head>
<body>

<!-- header -->
<div class="abs topbar"></div>
<div class="abs lang"><span class="flag" role="img" aria-label="English flag"></span><span class="caret"></span></div>
<div class="abs brand">KVR</div>
<div class="abs call">
  <svg width="26" height="26" viewBox="0 0 24 24" fill="none" stroke="#444" stroke-width="1.5"><path d="M5 3h4l2 5-2.5 1.5a11 11 0 0 0 6 6L16 13l5 2v4a2 2 0 0 1-2 2A17 17 0 0 1 3 5a2 2 0 0 1 2-2z"/></svg>
  <div><small>Call Us</small><b>+49 (0) 987654321</b></div>
</div>

<!-- hero -->
<svg class="abs hero" width="1200" height="670" viewBox="0 0 1200 670">
  <defs><linearGradient id="heroGrad" x1="0" y1="0" x2="1" y2="1"><stop offset="0" stop-color="#0a6e9e"/><stop offset="1" stop-color="#035f8c"/></linearGradient></defs>
  <path d="M0 0H1200V585Q900 620 600 630T0 668Z" fill="url(#heroGrad)"/>
  <path d="M0 668Q600 600 1200 585V600Q700 605 0 670Z" fill="#07476e"/>
  <circle cx="829" cy="333" r="190" fill="none" stroke="#0a93c4" stroke-width="9"/>
  <circle cx="829" cy="333" r="178" fill="#fff"/>
  <circle cx="829" cy="333" r="130" fill="url(#motorGrad)" role="img" aria-label="Planetary gear motor product photo"/>
  <defs><radialGradient id="motorGrad"><stop offset="0" stop-color="#3a4a58"/><stop offset=".6" stop-color="#8e9aa5"/><stop offset="1" stop-color="#fff"/></radialGradient></defs>
  <path d="M465 541l-8 10 8 10" fill="none" stroke="#fff" stroke-width="2.5"/>
  <path d="M724 541l8 10-8 10" fill="none" stroke="#fff" stroke-width="2.5"/>
  <circle cx="521" cy="551" r="30" fill="#cfd8de" stroke="#fff" stroke-width="3"/>
  <circle cx="599" cy="551" r="36" fill="#b8c4cc" stroke="#fff" stroke-width="4"/>
  <circle cx="678" cy="551" r="30" fill="#cfd8de" stroke="#fff" stroke-width="3"/>
</svg>
<nav class="abs nav"><span>Home</span><span class="dd">Gearboxes &amp; Motors</span><span class="dd">Engine Components</span><span class="dd">Drawing parts</span><span class="dd">Machines &amp; Accessories</span><span>About Us</span><span>Contact</span></nav>
<h1 class="abs hero-title">Your Competent Partner<br>For Industrial Engines</h1>
<p class="abs hero-sub">Transmission And Drawing Parts<br>With More Than 5000 Satisfied Customers</p>
<div class="abs btn-hero">Learn More</div>

<!-- why choose us -->
<h2 class="abs section-title" style="top:808px;font-size:46px">Why Choose Us</h2>
<p class="abs why-text">Lorem Ipsum is simply dummy text of the printing and typesetting industry. Lorem Ipsum has been the industry's standard dummy text ever since the 1500s Lorem Ipsum is simply dummy text of the printing and typesetting industry.</p>
<div class="abs feature" style="left:195px">
  <svg width="94" height="94" viewBox="0 0 94 94"><circle cx="47" cy="47" r="45" fill="none" stroke="var(--blue)" stroke-width="2"/><circle cx="47" cy="47" r="38" fill="var(--blue)"/><circle cx="47" cy="37" r="9" fill="none" stroke="#fff" stroke-width="3"/><path d="M31 60q16-18 32 0" fill="none" stroke="#fff" stroke-width="3"/></svg>
  <span>Customer<br>Satisfaction</span></div>
<div class="abs feature" style="left:488px">
  <svg width="94" height="94" viewBox="0 0 94 94"><circle cx="47" cy="47" r="45" fill="none" stroke="var(--blue)" stroke-width="2"/><circle cx="47" cy="47" r="38" fill="var(--blue)"/><circle cx="47" cy="47" r="19" fill="none" stroke="#fff" stroke-width="3"/><text x="47" y="55" text-anchor="middle" fill="#fff" font-size="22" font-family="Open Sans">$</text></svg>
  <span>Optimal<br>Price</span></div>
<div class="abs feature" style="left:769px">
  <svg width="94" height="94" viewBox="0 0 94 94"><circle cx="47" cy="47" r="45" fill="none" stroke="var(--blue)" stroke-width="2"/><circle cx="47" cy="47" r="38" fill="var(--blue)"/><circle cx="47" cy="42" r="14" fill="none" stroke="#fff" stroke-width="3"/><path d="M38 53l-6 14 8-3 4 6 3-9M56 53l6 14-8-3-4 6-3-9" fill="none" stroke="#fff" stroke-width="2.5"/></svg>
  <span>High Quality<br>Performance</span></div>

<!-- products -->
<div class="abs products-bg"></div>
<h2 class="abs section-title" style="top:1275px;font-size:46px">Our Products</h2>
<div class="abs card" style="left:130px;top:1376px;width:300px;height:257px">
  <div class="img" role="img" aria-label="Gear motor product photo"></div><h3 style="top:190px">Product Category</h3><span class="pill" style="top:242px">Details</span></div>
<div class="abs card active" style="left:450px;top:1409px;width:300px;height:255px">
  <div class="img" role="img" aria-label="Right-angle gearbox product photo"></div><h3 style="top:191px">Product Category</h3><span class="pill" style="top:241px">Details</span></div>
<div class="abs card" style="left:771px;top:1376px;width:300px;height:257px">
  <div class="img" role="img" aria-label="Harmonic drive component photo"></div><h3 style="top:190px">Product Category</h3><span class="pill" style="top:242px">Details</span></div>
<span class="abs dot" style="left:562px"></span>
<span class="abs dot" style="left:583px;background:var(--blue);border-color:var(--blue)"></span>
<span class="abs dot" style="left:604px"></span>
<span class="abs dot" style="left:625px"></span>

<!-- trade exhibition -->
<h2 class="abs section-title" style="top:1930px;font-size:46px">Trade Exhibition</h2>
<div class="abs photo" style="left:133px;top:2024px;width:301px;height:199px;background:linear-gradient(135deg,#3a5c7a,#8a7a6a,#2c4d78)" role="img" aria-label="Crowded exhibition hall"></div>
<div class="abs tile" style="left:133px;top:2223px;width:301px;height:199px">
  <h3 style="top:20px">Trade Exhibition</h3><p style="top:52px">Lorem Ipsum is simply dummy text of the printing and typesetting industry.</p>
  <span class="tbtn ticket" style="left:29px;top:141px">Free tickets</span><span class="tbtn more" style="left:148px;top:141px">Details</span></div>
<div class="abs tile" style="left:451px;top:2024px;width:301px;height:199px">
  <h3 style="top:27px">Trade Exhibition</h3><p style="top:58px">Lorem Ipsum is simply dummy text of the printing and typesetting industry.</p>
  <span class="tbtn ticket" style="left:29px;top:142px">Free tickets</span><span class="tbtn more" style="left:150px;top:142px">Details</span></div>
<div class="abs photo" style="left:451px;top:2223px;width:301px;height:199px;background:linear-gradient(135deg,#1f4f8a,#6a8ab0,#1c3c70)" role="img" aria-label="Visitors walking through trade fair booths"></div>
<div class="abs photo" style="left:768px;top:2024px;width:302px;height:199px;background:linear-gradient(135deg,#9aa6a8,#d8dcd6,#5d7a70)" role="img" aria-label="Exhibition stands in a large hall"></div>
<div class="abs tile" style="left:768px;top:2223px;width:302px;height:199px">
  <h3 style="top:20px">Trade Exhibition</h3><p style="top:52px">Lorem Ipsum is simply dummy text of the printing and typesetting industry.</p>
  <span class="tbtn ticket" style="left:29px;top:141px">Free tickets</span><span class="tbtn more" style="left:148px;top:141px">Details</span></div>
<div class="abs view-more">View More</div>

<!-- ebook -->
<svg class="abs" style="left:0;top:2627px" width="1200" height="198" viewBox="0 0 1200 198">
  <rect width="1200" height="198" fill="var(--blue)"/>
  <path d="M0 0H320L376 99 320 198H0Z" fill="#e6f0f6"/>
  <path d="M320 0H336L392 99 336 198H320L376 99Z" fill="#fff"/>
  <path d="M205 12H318L360 99 318 186H205L163 99Z" fill="var(--navy)" stroke-linejoin="round"/>
  <g fill="none" stroke="#fff" stroke-width="2"><rect x="245" y="48" width="16" height="28" rx="2"/><rect x="263" y="58" width="18" height="16"/><path d="M266 63h12M266 67h12"/></g>
  <text x="261" y="128" text-anchor="middle" fill="#fff" font-size="25" font-family="Open Sans">Ebook</text>
</svg>
<h2 class="abs ebook-head">Lorem Ipsum is simply dummy text</h2>
<p class="abs ebook-sub">Lorem Ipsum has been the industry's standard dummy</p>
<div class="abs btn-dl">Download Now</div>

<!-- about -->
<div class="abs about-bg" style="background:linear-gradient(110deg,#c8ccd0 0%,#d89a4a 25%,#b8c0c6 55%,#8a9aa4 80%,#c4cbd0 100%)" role="img" aria-label="Blurred industrial robot arm in a factory"></div>
<div class="abs about-box">
  <h2>About Us</h2>
  <p>Lorem Ipsum is simply dummy text of the printing and typesetting industry. Lorem Ipsum has been the industry's standard dummy text ever since the 1500s</p>
  <p>Lorem Ipsum is simply dummy text of the printing and typesetting industry. Lorem Ipsum has been the industry's standard dummy text ever since the 1500s</p>
</div>

<!-- footer -->
<div class="abs footer"></div>
<div class="abs footer-bar"></div>
<div class="abs f-brand">KVR</div>
<span class="abs social" style="left:176px"></span>
<span class="abs social" style="left:214px"></span>
<span class="abs social" style="left:258px"></span>
<div class="abs f-col" style="left:414px;top:3570px">
  <h4>Contact Us</h4>
  <div class="f-row"><svg width="14" height="18" viewBox="0 0 14 18" fill="none" stroke="#fff" stroke-width="1.5"><path d="M7 17s6-6 6-10A6 6 0 0 0 1 7c0 4 6 10 6 10z"/><circle cx="7" cy="7" r="2"/></svg><span>48 Harlow Lane<br>Address 20417 TX</span></div>
  <div class="f-row"><svg width="16" height="16" viewBox="0 0 24 24" fill="#fff"><path d="M5 3h4l2 5-2.5 1.5a11 11 0 0 0 6 6L16 13l5 2v4a2 2 0 0 1-2 2A17 17 0 0 1 3 5a2 2 0 0 1 2-2z"/></svg><span>+49 (0) 987654321</span></div>
  <div class="f-row"><svg width="16" height="14" viewBox="0 0 16 14" fill="none" stroke="#fff" stroke-width="1.5"><rect x="1" y="1" width="14" height="12"/><path d="M1 1l7 6 7-6"/></svg><span>name@kvrmail.com</span></div>
</div>
<div class="abs f-col" style="left:642px;top:3570px">
  <h4>Company</h4>
  <div>Home</div><div>Gearboxes &amp; Motors</div><div>Engine Components</div><div>Drawing Parts</div><div>Machines &amp; Accessories</div>
</div>
<div class="abs f-col" style="left:862px;top:3572px;width:240px">
  <h4 style="font-weight:400">Stil have questions?</h4>
  <div style="line-height:22px">A representative will aswer your questions as soon as possible.</div>
</div>
<div class="abs btn-contact">
  <svg style="position:absolute;left:2px;top:2px" width="38" height="38" viewBox="0 0 38 38"><circle cx="19" cy="19" r="18" fill="#0a3552" stroke="#fff" stroke-width="1"/><path transform="translate(10 10) scale(.75)" d="M5 3h4l2 5-2.5 1.5a11 11 0 0 0 6 6L16 13l5 2v4a2 2 0 0 1-2 2A17 17 0 0 1 3 5a2 2 0 0 1 2-2z" fill="none" stroke="#fff" stroke-width="1.8"/></svg>
  <span style="position:absolute;left:60px">Contact Now</span>
</div>
<div class="abs copy">Copyright 2020 Kvr. All Rights Reserved.</div>
<div class="abs legal">Privacy Policy &nbsp; | &nbsp; Terms Of Services</div>

</body>
</html>
```